Bref créative
Business Card for ecommerce technology company
Circuitry Supply Partners, LLC.
Professional
Paul Dunmore
President
457 Ridgeback Ave.
Fernvale, QX 58204
mark@quorvix.com
www.quorvix.com
Please send Business card so I will be able to edit it for other employees

```html
<!DOCTYPE html>
<html lang="en">
<head>
<meta charset="utf-8">
<title>Quorvix Stationery</title>
<link href="https://fonts.googleapis.com/css2?family=Exo+2:wght@700&family=Open+Sans:wght@400;600&display=swap" rel="stylesheet">
<style>
  :root{
    --bg:#e9eaec;
    --paper:#ffffff;
    --blue:#1f6fd8;
    --blue-deep:#0b4fae;
    --blue-light:#5fa3f0;
    --ink:#27364a;
    --muted:#7a8595;
    --rule:#cfd5de;
  }
  *{margin:0;padding:0;box-sizing:border-box}
  html,body{width:1200px;height:936px;overflow:hidden;background:var(--bg)}
  body{position:relative;font-family:"Open Sans",Arial,sans-serif;color:var(--ink)}
  .sheet{position:absolute;background:var(--paper);overflow:hidden}
  .band{position:absolute;left:0;bottom:0;width:100%}
  .brand{display:flex;align-items:center;gap:8px}
  .brand-dot{border-radius:50%;background:var(--blue);flex:none}
  .brand-name{font-family:"Exo 2",Arial,sans-serif;font-weight:700;color:var(--blue-deep);letter-spacing:.02em;line-height:1}
  .brand-sub{font-size:7px;color:var(--muted)}
  .url{position:absolute;color:#fff;font-size:9px;letter-spacing:.25em}

  /* letterhead */
  .letterhead{left:190px;top:76px;width:380px;height:544px}
  .letterhead .brand{position:absolute;left:26px;top:32px}
  .letterhead .contact{position:absolute;right:30px;top:30px;font-size:6.5px;line-height:11px;color:var(--muted)}
  .contact span{display:block}
  .contact span::before{content:"";display:inline-block;width:5px;height:5px;border-radius:50%;background:var(--blue);margin-right:5px;vertical-align:middle}
  .letterhead .faint-mark{position:absolute;left:124px;top:260px;width:132px;height:132px;border-radius:50%;background:radial-gradient(circle,#e3ecfa,#c7d8f3);opacity:.7}

  /* folder */
  .folder{left:632px;top:50px;width:507px;height:595px}
  .folder .hero{position:absolute;left:0;right:0;top:196px;display:flex;flex-direction:column;align-items:center;gap:14px}
  .folder .hero .brand-dot{width:120px;height:120px}
  .folder .hero .brand-name{font-size:44px}
  .folder .hero .brand-sub{font-size:14px;color:var(--blue-deep)}

  /* business cards */
  .card{left:46px;width:182px;height:105px}
  .card-front{top:653px}
  .card-front .brand{position:absolute;left:10px;top:12px}
  .card-front .person{position:absolute;right:12px;top:30px;text-align:right;font-size:6px;line-height:9px;color:var(--muted)}
  .card-front .person b{color:var(--ink);font-weight:600}
  .card-back{top:780px;height:100px}
  .card-back .mark{position:absolute;left:67px;top:18px;width:48px;height:48px;border-radius:50%;background:var(--blue)}
  .card-back .web{position:absolute;left:0;right:0;top:74px;text-align:center;font-size:6px;color:var(--muted);letter-spacing:.1em}

  /* envelopes */
  .envelope{top:663px;width:430px;height:198px}
  .envelope-front{left:266px}
  .envelope-front .brand{position:absolute;left:20px;top:22px}
  .envelope-front .return{position:absolute;left:20px;top:58px;font-size:6.5px;color:var(--muted)}
  .envelope-back{left:734px}
</style>
</head>
<body>

<section class="sheet letterhead">
  <div class="brand">
    <div class="brand-dot" style="width:28px;height:28px"></div>
    <div>
      <div class="brand-name" style="font-size:15px">QUORVIX</div>
      <div class="brand-sub">Circuitry Supply Partners, LLC.</div>
    </div>
  </div>
  <div class="contact">
    <span>457 Ridgeback Ave.</span>
    <span>Fernvale, QX 58204</span>
    <span>T 555 014 2290</span>
    <span>M 555 014 7731</span>
    <span>F 555 014 2291</span>
    <span>mark@quorvix.com</span>
    <span>www.quorvix.com</span>
  </div>
  <div class="faint-mark"></div>
  <svg class="band" viewBox="0 0 380 40" height="40" preserveAspectRatio="none">
    <rect x="0" y="20" width="380" height="3" fill="var(--ink)"/>
    <path d="M200 22 Q215 8 240 8 H380 V40 H180 Q195 36 200 22Z" fill="var(--blue)"/>
  </svg>
  <div class="url" style="right:20px;bottom:18px">www.quorvix.com</div>
</section>

<section class="sheet folder">
  <div class="hero">
    <div class="brand-dot"></div>
    <div class="brand-name">QUORVIX</div>
    <div class="brand-sub">Circuitry Supply Partners, LLC.</div>
  </div>
  <svg class="band" viewBox="0 0 507 62" height="62" preserveAspectRatio="none">
    <rect x="0" y="30" width="507" height="4" fill="var(--ink)"/>
    <path d="M250 32 Q270 10 305 10 H507 V62 H225 Q245 54 250 32Z" fill="var(--blue)"/>
  </svg>
  <div class="url" style="right:40px;bottom:24px;font-size:11px">www.quorvix.com</div>
</section>

<section class="sheet card card-front">
  <div class="brand">
    <div class="brand-dot" style="width:16px;height:16px"></div>
    <div class="brand-name" style="font-size:11px">QUORVIX</div>
  </div>
  <div class="person">
    <b>Paul Dunmore</b><br>President<br>555 014 2290<br>mark@quorvix.com
  </div>
  <svg class="band" viewBox="0 0 182 16" height="16" preserveAspectRatio="none">
    <rect x="0" y="8" width="182" height="1.5" fill="var(--ink)"/>
    <path d="M90 9 Q97 3 108 3 H182 V16 H84 Q90 14 90 9Z" fill="var(--blue)"/>
  </svg>
</section>

<section class="sheet card card-back">
  <div class="mark"></div>
  <div class="web">www.quorvix.com</div>
</section>

<section class="sheet envelope envelope-front">
  <div class="brand">
    <div class="brand-dot" style="width:24px;height:24px"></div>
    <div>
      <div class="brand-name" style="font-size:14px">QUORVIX</div>
      <div class="brand-sub">Circuitry Supply Partners, LLC.</div>
    </div>
  </div>
  <div class="return">457 Ridgeback Ave. Fernvale, QX 58204</div>
</section>

<section class="sheet envelope envelope-back">
  <svg viewBox="0 0 430 198" width="430" height="198" style="position:absolute;left:0;top:0">
    <path d="M0 70 L215 110 L430 70 V198 H0Z" fill="#f4f6f9"/>
    <path d="M0 0 H430 V70 L215 110 L0 70Z" fill="var(--blue)"/>
    <path d="M0 0 H430 V34 Q215 20 0 34Z" fill="var(--blue-light)" opacity=".5"/>
  </svg>
  <div class="url" style="left:0;right:0;top:36px;text-align:center">www.quorvix.com</div>
</section>

</body>
</html>
```